Letterhead

We need a professional, compelling letterhead that can be used for print and email stationary. We have the logo and the letterhead styling and colors should blend seamlessly and be complimentary. Looking for something unique and thoughtful.
Updates

Reason: There are good ideas and am requesting changes to some ideas in order to make a final decision. Thank you for for submissions. Also, I have uploaded the ai file. Please use that file. Thank you.

If you cannot see the .ai version of the logo that I have tried to upload, please message me if you want to make changes to your submission or submit new design and I will send that file to you directly. This .ai will need to be used in order to ensure high quality printing. Thank you.

Target Market(s)

Clients. Business partners.

Industry/Entity Type

It Professional

Requirements
Must have
• Our logo incorporated. Also the phrase, or tag line - Where Ideas Take Root.
Should not have
• Not boring. Not typical. Not too busy.

```html
<!DOCTYPE html>
<html lang="en">
<head>
<meta charset="utf-8">
<title>Veridian Advisory Group LLC — Letterhead</title>
<link rel="stylesheet" href="https://fonts.googleapis.com/css2?family=PT+Sans:wght@400&family=Kalam:wght@400&display=swap">
<style>
  :root {
    --navy: #1c355e;
    --green: #2ea44f;
    --lavender: #c0bfcf;
    --mint: #cde5c8;
    --ink: #1f2a3a;
    --paper: #ffffff;
  }
  * { margin: 0; padding: 0; box-sizing: border-box; }
  html, body {
    width: 1200px;
    height: 1000px;
    overflow: hidden;
    background: var(--paper);
  }
  .letterhead {
    position: relative;
    width: 1200px;
    height: 1000px;
    font-family: "PT Sans", Arial, sans-serif;
    color: var(--ink);
  }
  .block { position: absolute; }

  .brand-mark {
    left: 26px; top: 22px;
    width: 68px; height: 68px;
    border-radius: 50%;
    background: var(--navy);
  }
  .header-post { left: 95px; top: 18px; width: 11px; height: 77px; background: var(--navy); }
  .header-rule { left: 106px; top: 67px; width: 527px; height: 8px; background: var(--green); }

  .brand-name {
    position: absolute;
    left: 340px;
    width: 288px;
    top: 22px;
    text-align: center;
    color: var(--navy);
    font-weight: 400;
    line-height: 1;
  }
  .brand-name .primary {
    display: block;
    font-size: 24px;
    letter-spacing: 10px;
    margin-right: -10px;
  }
  .brand-name .secondary {
    display: block;
    font-size: 20px;
    margin-top: -1px;
    letter-spacing: 0.3px;
  }

  .tagline {
    position: absolute;
    right: 569px;
    top: 76px;
    font-family: "Kalam", "Comic Sans MS", cursive;
    font-size: 17px;
    color: var(--navy);
  }

  .side-band-left { left: 22px; top: 97px; width: 73px; height: 798px; background: var(--lavender); }
  .side-band-right { left: 557px; top: 97px; width: 76px; height: 883px; background: var(--mint); }

  .footer-rule { left: 26px; top: 910px; width: 519px; height: 8px; background: var(--green); }
  .footer-post { left: 545px; top: 895px; width: 12px; height: 85px; background: var(--navy); }

  .website {
    position: absolute;
    right: 662px;
    top: 889px;
    font-size: 15px;
  }
  .contact {
    position: absolute;
    font-size: 12px;
    line-height: 16px;
    font-style: normal;
  }
  .contact-address { left: 38px; top: 926px; }
  .contact-email { left: 190px; top: 942px; }
  .contact-phone { left: 421px; top: 934px; font-size: 11.5px; }
  .contact-fax { left: 421px; top: 957px; font-size: 11.5px; }
</style>
</head>
<body>
  <main class="letterhead">
    <div class="block brand-mark" aria-hidden="true"></div>
    <div class="block header-post"></div>
    <div class="block header-rule"></div>

    <h1 class="brand-name">
      <span class="primary">VERIDIAN</span>
      <span class="secondary">Advisory Group LLC</span>
    </h1>
    <p class="tagline">Where Ideas Take Root</p>

    <div class="block side-band-left"></div>
    <div class="block side-band-right"></div>

    <p class="website">www.yourcompany.com</p>
    <div class="block footer-rule"></div>
    <div class="block footer-post"></div>

    <address class="contact contact-address">
      ADDRESS:<br>222 Your Address St.<br>City Name, State 2222
    </address>
    <p class="contact contact-email">EMAIL: email@yourcompany.com</p>
    <p class="contact contact-phone">PHONE: 111-111-1111</p>
    <p class="contact contact-fax">FAX: 111-111-1111</p>
  </main>
</body>
</html>
```